Design for a Note buying company that attracts landlords and seller financed notes

I need a card designed. I want a simple clean front with my logo and contact info. On the back I want some big and bold words to get a message across.

Our Company buys Notes (mortgages) and we want to convey the sense of financial security. Our number one market that we pursue is tired landlords.

If you want to understand our business you can visit our website. www.lakeviewpaperfund.com

Do not use any Clip Art in the design, it will not be accepted. I want a custom designed card not something I could throw together myself. Simple clean and drive the message home.

Target Market(s)

Landlords, seller financed note holders

Industry/Entity Type

Mortgage

Contact Information for Business Card

Simple clean and bold. I need to grab the attention of the customer. It should convey a professional touch.

Font styles to use
Sans Serif

Colors
ec2229
ffffff

Requirements
Must have
• Clean front with logo and contact information
Front colors should match logo

Back should be bold and grab attention. Back colors are open to ideas
Nice to have
• The Back May use the phrase "No more Tentants, No more Toilets" "More Time, More Cash"

I'm open to other ideas about grabbing a landlords attention

I'm open to a square card design
I like cards with round corners as well
Should not have
• any clip art! must be custom designs.

```html
<!DOCTYPE html>
<html lang="en">
<head>
<meta charset="utf-8">
<title>Lakeview Paper Fund – Square Business Card</title>
<link rel="stylesheet" href="https://fonts.googleapis.com/css2?family=Lato:wght@400;700&family=Saira:wght@700;800&family=Source+Sans+3:wght@700&display=swap">
<style>
  :root {
    --page-bg: #e3e3e3;
    --card-dark: #08090b;
    --card-light: #f4f4f4;
    --brand-red: #ec2229;
    --ink: #111111;
    --white: #ffffff;
  }
  * { margin: 0; padding: 0; box-sizing: border-box; }
  html, body {
    width: 1200px;
    height: 960px;
    overflow: hidden;
    background: var(--page-bg);
  }
  .canvas {
    position: relative;
    width: 1200px;
    height: 960px;
  }
  .card {
    position: absolute;
    top: 292px;
    width: 376px;
    height: 376px;
    border-radius: 18px;
  }
  .card--back {
    left: 202px;
    background: var(--card-dark);
    display: flex;
    align-items: center;
    justify-content: center;
  }
  .back-slogan {
    font-family: "Source Sans 3", "Source Sans Pro", sans-serif;
    font-weight: 700;
    font-size: 34px;
    line-height: 37px;
    color: var(--white);
    text-align: left;
    letter-spacing: 0.3px;
    margin-top: 14px;
  }
  .card--front {
    left: 625px;
    background: var(--card-light);
    text-align: center;
    color: var(--ink);
  }
  .tagline {
    position: absolute;
    top: 32px;
    left: 0;
    right: 0;
    font-family: "Saira", sans-serif;
    font-weight: 800;
    font-size: 12px;
    letter-spacing: 4.2px;
  }
  .brand-name {
    position: absolute;
    top: 88px;
    left: 0;
    right: 0;
    font-family: "Saira", sans-serif;
    font-weight: 800;
    font-size: 27px;
    letter-spacing: 1.5px;
    line-height: 34px;
    color: var(--ink);
  }
  .contact {
    position: absolute;
    top: 196px;
    left: 0;
    right: 0;
    font-family: "Lato", sans-serif;
  }
  .contact__name {
    font-weight: 700;
    font-size: 16.5px;
    letter-spacing: 0.4px;
    color: var(--brand-red);
    line-height: 20px;
  }
  .contact__role {
    font-size: 13.5px;
    line-height: 18px;
  }
  .contact__address {
    margin-top: 20px;
    font-size: 13.5px;
    line-height: 18px;
  }
  .contact__icons {
    display: flex;
    justify-content: center;
    gap: 8px;
    margin-top: 6px;
    height: 14px;
  }
  .contact__icons svg { width: 14px; height: 14px; display: block; }
  .contact__line {
    font-size: 13.5px;
    line-height: 18px;
  }
  .contact__lines { margin-top: 2px; }
  .web-highlight { color: var(--brand-red); font-weight: 700; }
</style>
</head>
<body>
<div class="canvas">

  <section class="card card--back" aria-label="Card back">
    <p class="back-slogan">MORE TIME<br>MORE CASH</p>
  </section>

  <section class="card card--front" aria-label="Card front">
    <p class="tagline">WE HELP PEOPLE LIVE!</p>
    <p class="brand-name">LAKEVIEW PAPER FUND</p>

    <div class="contact">
      <p class="contact__name">DANIEL CARVER</p>
      <p class="contact__role">Founder</p>
      <p class="contact__address">P.O. Box 218, Millbrook, Kansas 67150</p>

      <div class="contact__icons" aria-hidden="true">
        <svg viewBox="0 0 14 14">
          <circle cx="7" cy="7" r="7" fill="var(--brand-red)"/>
          <path d="M4.3 3.6c.4-.3.8-.2 1 .2l.6 1.2c.2.3.1.6-.2.8l-.4.3c.3.8 1 1.6 1.9 2l.3-.4c.2-.3.5-.3.8-.2l1.2.6c.4.2.5.6.2 1l-.5.6c-.4.4-1 .5-1.6.2C6 9.3 4.7 8 4 6.4c-.3-.6-.2-1.2.2-1.6z" fill="var(--white)"/>
        </svg>
        <svg viewBox="0 0 14 14">
          <circle cx="7" cy="7" r="7" fill="var(--brand-red)"/>
          <rect x="3.5" y="4.6" width="7" height="4.8" rx="0.6" fill="var(--white)"/>
          <path d="M3.7 4.9 7 7.4l3.3-2.5" stroke="var(--brand-red)" stroke-width="0.8" fill="none"/>
        </svg>
        <svg viewBox="0 0 14 14">
          <circle cx="7" cy="7" r="7" fill="var(--brand-red)"/>
          <g stroke="var(--white)" stroke-width="0.8" fill="none">
            <circle cx="7" cy="7" r="3.6"/>
            <ellipse cx="7" cy="7" rx="1.6" ry="3.6"/>
            <path d="M3.4 7h7.2M4 5.2h6M4 8.8h6"/>
          </g>
        </svg>
      </div>

      <div class="contact__lines">
        <p class="contact__line">316-555-0142</p>
        <p class="contact__line">info@lakeviewpaperfund.com</p>
        <p class="contact__line">www.<span class="web-highlight">lakeviewpaperfund</span>.com</p>
      </div>
    </div>
  </section>

</div>
</body>
</html>
```